Hulls For Trade Website makeover

Hulls For Trade is in need of a makeover. It is feeling tired and needs a fresh new look and feel as well as being user friendly.

Hulls For Trade is an industry owned marketplace website for the sale of recreational boats, marina berths, chandlery, water craft like kayaks - anything related to recreation on the water. The main focus however is boats - new and used. The site is only available to industry businesses so no private sales are available on the site.

This approach ensures that the buyers know that title is guaranteed to all boats sold and that the businesses are reputable and stand behind their products.

The current site address is www.hullsfortrade.example.au

Target Market(s)

The target market are people interested in outdoor recreation - boaters, kayakers, sailors, paddle boarders, those looking for marina berths for their boat and those looking for service providers.

It should appeal to families, males and females, sports oriented people, fishermen, and those just looking for a relaxing, outdoor, healthy lifestyle.

Requirements
Must have
• Be very user friendly, intuitive in terms of searching, be uncluttered, fresh and engaging.
• Marine recreation is about lifestyle, fun and relaxation. When people buy a boat they are buying into a desirable, healthy lifestyle.
• It must present as professional and give consumers confidence about the professionalism of the businesses selling their products on the site.
Nice to have
• Good images that portray the lifestyle in the Australian marketplace.
• Cater for the needs of sellers to be able to showcase their products to consumers.
Should not have
• Be cluttered and hard to navigate.

```html
<!DOCTYPE html>
<html lang="en">
<head>
<meta charset="utf-8">
<title>Hulls For Trade</title>
<link href="https://fonts.googleapis.com/css2?family=Arimo:wght@400;700&family=Roboto+Condensed:wght@400;700&display=swap" rel="stylesheet">
<style>
:root{
  --blue:#1a6fb8;
  --blue-dark:#14569c;
  --blue-nav:#92c3e8;
  --blue-active:#1a80d2;
  --blue-btn:#a3cff0;
  --text:#555;
  --line:#c9c9c9;
  --footer:#3b3b3b;
}
*{margin:0;padding:0;box-sizing:border-box}
html,body{width:682px;height:1200px;overflow:hidden;background:#fff}
body{font-family:"Arimo",Arial,sans-serif;color:var(--text);position:relative}
.abs{position:absolute}
.brand{left:49px;top:28px;display:flex;align-items:center;gap:8px;color:var(--blue-dark);font-weight:700;font-size:22px;letter-spacing:-.3px}
.brand .mark{width:26px;height:26px;background:var(--blue)}
.site-search{left:483px;top:40px;width:148px;height:20px;border:1px solid #ccc;font-size:8px;color:#999;padding:5px 7px}
.site-search svg{position:absolute;right:6px;top:5px}
.nav{left:0;top:85px;width:682px;height:28px;background:var(--blue-nav);display:flex;padding-left:51px;font-family:"Roboto Condensed",sans-serif;font-size:10px;color:#fff}
.nav a{color:#fff;text-decoration:none;padding:0 12px;line-height:28px;border-right:1px solid rgba(255,255,255,.45)}
.nav a:last-child{border-right:0}
.nav a.active{background:var(--blue-active)}
.hero{left:0;top:113px;width:682px;height:276px;background:linear-gradient(180deg,#a9c3d9 0%,#c7d6e2 35%,#2d4d6c 50%,#162c45 100%)}
.caption{left:49px;top:316px;height:38px;padding:0 12px;background:rgba(40,40,40,.65);color:#fff;font-weight:700;font-size:12.5px;line-height:38px}
.dots{left:603px;top:369px;display:flex;gap:2px}
.dots i{width:7px;height:7px;border:1px solid #fff;border-radius:50%;display:block}
.dots i:first-child{background:#fff}
.panel{left:49px;top:407px;width:375px;height:380px;border:1px solid var(--line)}
h2,h3{font-weight:400;color:var(--blue)}
.lbl{color:var(--blue);font-size:10px}
.field{border:1px solid #ccc;background:linear-gradient(#fff,#f1f1f1);height:23px}
.select{font-size:9px;color:#555;padding:5px 8px}
.select::after{content:"";position:absolute;right:7px;top:9px;border:3px solid transparent;border-top:4px solid #777}
.btn{color:#fff;font-size:10px;text-align:center;line-height:23px}
.btn.light{background:var(--blue-btn)}
.btn.dark{background:var(--blue-dark)}
.small{font-size:8px;line-height:14.5px;color:#555}
.body-text{left:49px;top:832px;width:378px;font-size:7.6px;line-height:14.2px}
.body-text p{margin-bottom:4px}
.news-item{left:466px;width:170px}
.news-item h4{font-weight:400;color:var(--blue);font-size:9.2px;display:flex;align-items:center;gap:6px}
.news-item h4::before{content:"";width:7px;height:7px;border-radius:50%;background:#888}
.news-item p{font-size:7.2px;line-height:14.4px;color:#666;padding-left:14px;margin-top:3px}
.ad{left:466px;width:167px}
.divider-shadow{left:140px;top:1020px;width:400px;height:8px;background:radial-gradient(ellipse at center top,rgba(0,0,0,.12),transparent 70%)}
.badges{left:49px;top:1046px;width:584px;display:flex;justify-content:space-between;align-items:center}
.badge{background:#d6e2ee;height:44px}
.footer{left:0;top:1124px;width:682px;height:76px;background:var(--footer);color:#ddd;font-size:7.4px}
.social{display:flex;gap:8px;position:absolute;right:76px;top:28px}
.social i{width:20px;height:20px;display:block}
</style>
</head>
<body>

<div class="abs brand"><span class="mark"></span>Hulls For Trade</div>
<div class="abs site-search">Search..
  <svg width="9" height="9" viewBox="0 0 10 10"><circle cx="4" cy="4" r="3" fill="none" stroke="#888" stroke-width="1.3"/><line x1="6.3" y1="6.3" x2="9" y2="9" stroke="#888" stroke-width="1.3"/></svg>
</div>

<nav class="abs nav">
  <a class="active">HOME</a><a>BOATS FOR SALE</a><a>NEW BOATS</a><a>MARINE</a><a>ACCESSORIES</a><a>MARINE PRODUCTS</a><a>SERVICES</a><a>CONTACT US</a>
</nav>

<div class="abs hero" role="img" aria-label="White motor cruiser speeding across dark blue sea beneath a cloudy sky, lighthouse on a rocky headland"></div>
<div class="abs caption">MAKE YOUR NEXT INVESTMENT ONE THAT IS SUPPORTED BY YOUR LOCAL MTC.</div>
<div class="abs dots"><i></i><i></i><i></i><i></i></div>

<section class="abs panel"></section>
<h2 class="abs" style="left:62px;top:419px;font-size:13px">NEW AND USED BOATS FOR SALE</h2>
<div class="abs" style="left:59px;top:461px;font-size:12.5px;color:var(--blue)">Quick search</div>
<div class="abs field" style="left:145px;top:457px;width:174px;height:24px;background:#fff"></div>
<div class="abs btn light" style="left:330px;top:457px;width:78px;height:24px;line-height:24px">SEARCH</div>
<div class="abs lbl" style="left:59px;top:495px">OR Select your state/s, a price range and new/used</div>
<div class="abs" role="img" aria-label="Map of Australia divided into selectable states" style="left:58px;top:523px;width:78px;height:72px;background:#7fb0dc;border-radius:40% 45% 35% 50%"></div>
<div class="abs lbl" style="left:156px;top:535px">New and /or used</div>
<div class="abs lbl" style="left:156px;top:566px">Price from</div>
<div class="abs lbl" style="left:156px;top:598px">Price to</div>
<div class="abs field select" style="left:244px;top:528px;width:133px">New and used boats</div>
<div class="abs field select" style="left:244px;top:559px;width:133px">0</div>
<div class="abs field select" style="left:244px;top:591px;width:133px">all</div>
<div class="abs btn light" style="left:297px;top:626px;width:78px">SEARCH</div>
<div class="abs" style="left:58px;top:674px;width:354px;border-top:1px solid #ddd"></div>
<h3 class="abs" style="left:61px;top:688px;font-size:13px">WANT US TO DO THE SEARCHING FOR YOU?</h3>
<p class="abs small" style="left:61px;top:709px;width:355px">Register now! We can email you when boats are listed that match your criteria. We can also alert our members with what you are looking for. Its that easy!</p>
<div class="abs btn dark" style="left:278px;top:742px;width:132px">Register for email alerts</div>

<h3 class="abs" style="left:49px;top:809px;font-size:12.5px">Boats for Sale backed by the Marine Trades Council</h3>
<div class="abs body-text">
  <p>The Marine Trades Council and their network of members welcome you to the only marine marketplace website offering the largest range of boats for sale and other marine related products, backed by the association quality assurance programs.</p>
  <p>When you deal with the professionals of the marine industry you are assured of highest possible standard of service and product quality. All marine industry members are bound by the code of conduct and ethics, set down by their Industry Association.</p>
  <p>hullsfortrade.example.au is owned and operated by the Marine Trades Council and offers the consumer the benefit of making their purchase with the utmost confidence, from expert marine focused members, offering quality products and service.</p>
</div>
<div class="abs" style="left:378px;top:971px;font-size:8px;color:var(--blue)">Read more..</div>

<h3 class="abs" style="left:466px;top:407px;font-size:12.5px">Latest News</h3>
<div class="abs news-item" style="top:433px"><h4>Selling on High seas</h4><p>A new marketing initiative promoting the beauty and accessibility of the Southern Great Barrier Reef will roll out this month</p></div>
<div class="abs news-item" style="top:507px"><h4>Selling on High seas</h4><p>A new marketing initiative promoting the beauty and accessibility of the Southern Great Barrier Reef will roll out this month</p></div>

<div class="abs ad" role="img" aria-label="Buyers beware advert: outboard engines on a blue background" style="top:592px;height:278px;background:linear-gradient(180deg,#7da5c8 0%,#1f4ea3 30%,#1d4b9e 100%)"></div>
<div class="abs" style="left:474px;top:715px;width:151px;text-align:center;color:#fff;font-weight:700;font-size:11.5px;line-height:14.5px">Things you need to know before you buy an imported boat or engine</div>
<div class="abs ad" style="top:884px;height:94px;background:linear-gradient(180deg,#f08a2a 0 47%,#1d4fb0 47% 64%,#8fb8de 64%)" role="img" aria-label="Advert for new and used boats from Harbour Motor Craft"></div>
<div class="abs" style="left:474px;top:898px;font-size:12px;font-weight:700;color:#1d4fb0">Harbour Motor Craft</div>
<div class="abs" style="left:480px;top:928px;font-size:12px;font-weight:700;color:#fff">New &amp; Used Boats</div>

<div class="abs divider-shadow"></div>
<div class="abs badges">
  <div class="badge" style="width:62px"></div>
  <div class="badge" style="width:100px;height:34px"></div>
  <div class="badge" style="width:28px"></div>
  <div class="badge" style="width:100px;height:36px"></div>
  <div class="badge" style="width:52px"></div>
  <div class="badge" style="width:64px"></div>
  <div class="badge" style="width:51px;background:#2a4f9e"></div>
</div>

<footer class="abs footer">
  <div class="abs" style="left:50px;top:27px">Privacy Policy | Terms and Conditions</div>
  <div class="abs" style="left:50px;top:46px">Copyrights 2013. All Rights Reserved.</div>
  <div class="social"><i style="background:#3b5bb0"></i><i style="background:#2a9ee0"></i><i style="background:#f07a22"></i><i style="background:#d7282a"></i></div>
</footer>

</body>
</html>
```